Business Card Design

Hello Designer,
This is an internet based company. We specialize in low rate advertisement space on a number of our websites, Similar to wandertally. We also Do keyword seo, social media development and management, website development,and mobile friendly reformatting of websites. The overall design should communicate Plume Harbor provides customers with easy access to our advertised businesses, to connect businesses to their desired customers and vice versa.
Updates

Hello Designers!,

If you would like to view my website for ideas please visit. sarasotaplume.example
Also I would like the "PLUME HARBOR" lettering to be different colors, like Zentrix's lettering. Also the color scheme I was thinking was blue, white, black
Thank you for taking on this project,
DorianĀ 

Industry/Entity Type

Internet

Contact Information for Business Card

Plume Harbor,Dorian Falkstead,CEO, dorian@plumehbr.example, CELL: 941-552-0318, 4182 Larkmoor Ln Sarasota 34231,dorian@plumehbr.example, Making The Internet More Affordable and Manageable,sarasotaplume.example
ON BACK: Making The Internet More Affordable and Manageable, sarasotaplume,tampaplume,miamiplume,pensacolaplume,jacksonvilleplume, and more, many more.

```html
<!DOCTYPE html>
<html lang="en">
<head>
<meta charset="utf-8">
<title>Plume Harbor Business Card</title>
<link rel="stylesheet" href="https://fonts.googleapis.com/css2?family=Questrial&display=swap">
<style>
  :root {
    --backdrop: #e9e6e1;
    --card-white: #ffffff;
    --card-black: #0b0d10;
    --card-black-soft: #1b1f25;
    --accent-blue: #1e86c8;
    --accent-blue-bright: #2fa3e6;
    --ink: #111111;
    --ink-soft: #333333;
  }
  * { margin: 0; padding: 0; box-sizing: border-box; }
  html, body {
    width: 1200px; height: 784px; overflow: hidden;
    background: var(--backdrop);
    font-family: "Questrial", "Century Gothic", sans-serif;
  }
  .canvas {
    position: relative; width: 1200px; height: 784px;
    display: flex; align-items: center; justify-content: center; gap: 40px;
  }
  .card {
    position: relative; width: 540px; height: 310px;
    border-radius: 4px; overflow: hidden;
    box-shadow: 0 10px 28px rgba(0,0,0,.18);
  }

  /* Back side */
  .card-back {
    background: radial-gradient(ellipse at 50% 40%, var(--card-black-soft), var(--card-black) 75%);
    color: var(--accent-blue-bright);
    display: flex; flex-direction: column; align-items: center; justify-content: center;
    text-align: center; gap: 6px;
  }
  .card-back .tagline { font-size: 18px; letter-spacing: .2px; margin-bottom: 4px; }
  .card-back .site { font-size: 19px; letter-spacing: .3px; }

  /* Front side */
  .card-front { background: var(--card-white); color: var(--ink); }
  .brand {
    position: absolute; left: 30px; top: 34px;
    display: flex; align-items: center; gap: 12px;
  }
  .brand-mark {
    width: 44px; height: 44px; border-radius: 50%;
    background: var(--accent-blue);
  }
  .brand-name {
    font-size: 38px; color: var(--ink); letter-spacing: 1px; line-height: 1;
  }
  .brand-site {
    position: absolute; left: 88px; top: 88px;
    font-size: 22px; color: var(--accent-blue);
  }
  .person { position: absolute; left: 40px; top: 138px; }
  .person-name { font-size: 21px; color: var(--accent-blue); }
  .person-title { font-size: 12px; color: var(--ink-soft); margin-top: 2px; }
  .contact-list {
    position: absolute; left: 40px; top: 190px; list-style: none;
    display: flex; flex-direction: column; gap: 3px;
  }
  .contact-list li {
    display: flex; align-items: center; gap: 8px;
    font-size: 16px; color: var(--ink);
  }
  .contact-list svg { width: 16px; height: 16px; flex: none; }
  .footer-rule {
    position: absolute; left: 0; right: 0; bottom: 30px; height: 3px;
    background: var(--accent-blue);
  }
  .footer-band {
    position: absolute; left: 0; right: 0; bottom: 0; height: 30px;
    background: var(--card-black);
    display: flex; align-items: center; justify-content: center;
    color: var(--accent-blue-bright); font-size: 11px; letter-spacing: 4px;
    text-transform: uppercase;
  }
</style>
</head>
<body>
<main class="canvas">

  <section class="card card-back" aria-label="Card back">
    <p class="tagline">Making The Internet More Affordable and Manageable</p>
    <p class="site">sarasotaplume.example</p>
    <p class="site">tampaplume.example</p>
    <p class="site">miamiplume.example</p>
    <p class="site">pensacolaplume.example</p>
    <p class="site">jacksonvilleplume.example</p>
    <p class="site">and more, many more</p>
  </section>

  <section class="card card-front" aria-label="Card front">
    <div class="brand">
      <span class="brand-mark"></span>
      <span class="brand-name">PLUME HARBOR</span>
    </div>
    <p class="brand-site">Sarasotaplume.example</p>

    <div class="person">
      <p class="person-name">Dorian Falkstead</p>
      <p class="person-title">CEO</p>
    </div>

    <ul class="contact-list">
      <li>
        <svg viewBox="0 0 16 16" aria-hidden="true"><rect x="4" y="1" width="8" height="14" rx="1.5" fill="#1e86c8"/><rect x="5.5" y="3" width="5" height="8" fill="#fff"/></svg>
        941-552-0318
      </li>
      <li>
        <svg viewBox="0 0 16 16" aria-hidden="true"><rect x="1" y="3" width="14" height="10" rx="1" fill="#1e86c8"/><path d="M1.5 3.5 8 9l6.5-5.5" fill="none" stroke="#fff" stroke-width="1.3"/></svg>
        dorian@plumehbr.example
      </li>
      <li>
        <svg viewBox="0 0 16 16" aria-hidden="true"><circle cx="8" cy="8" r="6.5" fill="none" stroke="#1e86c8" stroke-width="1.4"/><ellipse cx="8" cy="8" rx="3" ry="6.5" fill="none" stroke="#1e86c8" stroke-width="1.2"/><path d="M1.5 8h13" stroke="#1e86c8" stroke-width="1.2"/></svg>
        sarasotaplume.example
      </li>
      <li>
        <svg viewBox="0 0 16 16" aria-hidden="true"><path d="M8 1.5 1 8h2v6.5h4v-4h2v4h4V8h2z" fill="#1e86c8"/></svg>
        4182 Larkmoor Ln Sarasota 34231
      </li>
    </ul>

    <div class="footer-rule"></div>
    <div class="footer-band">Making the internet more affordable and manageable</div>
  </section>

</main>
</body>
</html>
```